Unternehmensberatung sucht Kartendesign für Seminarspiel
Zielgruppe
Projekt: Kartenspiel Seminarspiel für Führungskräfte / Trainerbedarf
Wir sind eine Unternehmensberatung, die Führungskräfte und Unternehmen in Veränderungsprozessen begleitet.
Aufgabenstellung
Desgin: in DIN A6 als Druckvorlage bzw. zur Verwendung der Bilddateien.
ZU designen: 1 Rückseite:
ca. 9 Vorderseiten-Designs, div. Texte -> 60 Seiten
1 Verpackung

```html
<!DOCTYPE html>
<html lang="de">
<head>
<meta charset="utf-8">
<title>Seminarspiel – Kartendesign</title>
<link rel="stylesheet" href="https://fonts.googleapis.com/css2?family=Arimo:wght@400;700&display=swap">
<style>
  :root {
    --stage: #737373;
    --white: #ffffff;
    --ink: #111111;
    --staerken: #214e94;
    --vertrauen: #3573b9;
    --resilienz: #005ea7;
  }
  * { margin: 0; padding: 0; box-sizing: border-box; }
  html, body { width: 1200px; height: 648px; overflow: hidden; }
  body {
    position: relative;
    background: var(--stage);
    font-family: "Arimo", Arial, sans-serif;
  }
  .card {
    position: absolute;
    width: 318px;
    height: 226px;
    overflow: hidden;
  }
  .card--front { background: var(--white); }
  .card--front .band {
    position: absolute;
    left: 0; top: 0;
    width: 318px; height: 226px;
  }
  .task {
    position: absolute;
    left: 14px; right: 14px; top: 23px;
    text-align: center;
    color: var(--ink);
    font-size: 13.8px;
    line-height: 15.3px;
  }
  .fact {
    position: absolute;
    left: 22px; right: 22px;
    text-align: center;
    color: var(--white);
    font-size: 7.4px;
    line-height: 8.5px;
  }
  .card--back {
    display: flex;
    flex-direction: column;
    align-items: center;
    justify-content: center;
    color: var(--white);
  }
  .icon {
    width: 45px; height: 45px;
    border: 2px solid var(--white);
    background: linear-gradient(135deg, rgba(255,255,255,.75), rgba(255,255,255,.45));
    margin-bottom: 9px;
  }
  .card-title {
    font-weight: 700;
    font-size: 33px;
    line-height: 35px;
    text-align: center;
  }
  .theme-staerken { --c: var(--staerken); }
  .theme-vertrauen { --c: var(--vertrauen); }
  .theme-resilienz { --c: var(--resilienz); }
  .card--back { background: var(--c); }
  .band path { fill: var(--c); }
</style>
</head>
<body>

  <!-- Vorderseiten -->
  <article class="card card--front theme-staerken" style="left:55px; top:84px;">
    <svg class="band" viewBox="0 0 318 226" aria-hidden="true"><path d="M0 145 Q159 181 318 145 L318 226 L0 226 Z"/></svg>
    <p class="task">a.<br>Stärkenbrille: Fokussiere Dich in Deinen Gesprächen darauf, Deinem Gesprächspartner am Ende eine wertvolle Stärke zurückzumelden, die Dir an Ihm auffällt.</p>
    <p class="fact" style="top:172px; left:24px; right:20px;">Sorge dafür, dass Deine Mitarbeiter bei der Arbeit das tun können, was sie am besten können! Der Stärkenfokus ist zentral im Positive Leadership-Ansatz und hat, wenn konsequent angewandt, verschiedene positive Effekte in Unternehmen wie die Steigerung der Produktivität und des Wohlbefindens des Einzelnen, die Verbesserung der Mitarbeiterbindung und der Senkung des Krankenstandes.</p>
  </article>

  <article class="card card--front theme-vertrauen" style="left:439px; top:84px;">
    <svg class="band" viewBox="0 0 318 226" aria-hidden="true"><path d="M0 145 Q159 181 318 145 L318 226 L0 226 Z"/></svg>
    <p class="task">a.<br>Offenheit: Offenheit schafft Vertrauen. Fokussiere Dich auf etwas, das Dich gerade beschäftigt. Teile Deine Gedanken mit einer Person, die diese Offenheit von Deiner Seite bislang nicht kennt.</p>
    <p class="fact" style="top:185px;">Mit großem Abstand gehören im Nordwerk Projekt Kallisto Psychologische Sicherheit und Vertrauen zu den wichtigste Einflussfaktoren für die Entfaltung der Leistungsfähigkeit in Unternehmen.</p>
  </article>

  <article class="card card--front theme-resilienz" style="left:821px; top:88px;">
    <svg class="band" viewBox="0 0 318 226" aria-hidden="true"><path d="M0 146 Q159 182 318 146 L318 226 L0 226 Z"/></svg>
    <p class="task">a.<br>Verbessere die sozialen Beziehungen in Deinem Team. Was kannst Du dafür tun, um bessere und verbindlichere Beziehungen in Deinem Team zu schaffen?</p>
    <p class="fact" style="top:181px; left:18px; right:18px;">Wenn Menschen in belastenden Situationen psychisch stabil bleiben und sich von Rückschlägen zügig erholen, nennen Psychologen diese Fähigkeit "Resilienz". Resiliente Menschen sind beruflich erfolgreicher, emotional stabiler sowie körperlich und psychisch gesünder.</p>
  </article>

  <!-- Rückseiten -->
  <article class="card card--back theme-staerken" style="left:55px; top:332px;">
    <div class="icon" role="img" aria-label="Symbol: angespannter Oberarm mit Aufwärtspfeil"></div>
    <h2 class="card-title">Stärken</h2>
  </article>

  <article class="card card--back theme-vertrauen" style="left:439px; top:332px;">
    <div class="icon" role="img" aria-label="Symbol: zwei schützende Hände"></div>
    <h2 class="card-title">Sicherheit<br>und Vertrauen</h2>
  </article>

  <article class="card card--back theme-resilienz" style="left:821px; top:336px;">
    <div class="icon" role="img" aria-label="Symbol: biegsamer Bambusstab mit Blatt"></div>
    <h2 class="card-title">Resilienz</h2>
  </article>

</body>
</html>
```